Luxury Japanese Matcha Green Tea Packaging Full Packet Design

We're looking for a quality full pack design (front and back) for Ceremonial Grade and Premium Grade Matcha to sell on Bazaarly. We need a 2D versions of front and back images in photoshop and JPG. We also need a 3D versions of front and back for marketing purposes.

You can see our current styling and pack at www.leafwrights.co.uk. However, we want to improve the design and go more professional, simple and elegant with the brand. The last design was from 3 years a go. But hopefully you can see what we are about.

The design will be identical both both packs:

Pack 1: 230mm x 140mm - Premium Grade
Pack 2: 170mm x 120mm - Ceremonial Grade

The design needs to fit both sizes, with pack 1 saying Premium Grade and pack 2 saying Ceremonial Grade.

As many colours as needed, printing is CMYK + White digital printed.

Front of pack:

Product Headline:

Organic Handpicked
Stoneground Japanese Matcha
Green Tea Powder

抹茶

Text: Premium Grade (pack 1) / Ceremonial Grade (pack 2)

100g (pack 1) / 40g (pack 2)

(EU Organic logo)

Back of pack:

Organic Certified GB-ORG-17
Stone Ground Ceremonial Grade Matcha from Uji

Ingredients: 100% Organic Matcha Green Tea Powder

Place of origin: Japan, Store in a cool, dry, dark place
Keep sealed at all times, Best Before 31/03/2020
Not recommended for use if pregnant or nursing

Your next order is ready for you at www.BrewHour.co.uk

Preparing Traditional Matcha Tea:
Sift 1-2g or 1/2 teaspoon of Matcha Green Tea
powder into a bowl or large cup. Add 1/2 cup of hot water
at drinking temperature. Whisk with Bamboo or
Electric Whisk until frothy. Drink immediately.

Preparing Matcha Latte:
Sift 1-2g of Matcha Power into a cup, mix in 2-3 tablespoons of hot water.
Add hot milk and sweetener if desired. Whisk thoroughly.

Nutritional Information:

Per 1g Per 100g
Energy 14.44kJ 1446kJ
3.44kCal 345kCal
Fat 0.04g 4g
Saturates <0.01g 0.6g
Carbohydrates 0.76g 76g
of which sugars 0.47g 47.2g
Protein 0.144g 14.5g
Salt <0.01g 126mg

Per 1g Per 100g
Calcium 1.88mg 191mg
Potassium 94.8mg 3750mg
Iron <0.1g 1.6mg
Zinc <0.1g 1.72mg
Vitamin A 120µg (15% RDA) 2400µg (150% RDA)
Vitamin C 3mg (4% RDA) 60mg (75% RDA)
Folic acid 6µg (6% RDA) 60µg (30% RDA)
Riboflavin 0.1mg (4% RDA) 1.4mg (96% RDA)
Caffeine 17mg 1700mg

Copperfield Vale Ltd. T/A Leafwrights
Company Number: 05517268
Registered Office: 7 The Yard, Harrowden Way
Newbury, Berkshire, RG17 2PD
social@leafwrights.co.uk
Local Call +44 (0) 20 3185 6417 / Freephone +44 (0) 800 542 1736

This supplement should not be used as a substitute for a varied diet Do not exceed the recommended daily dose.

For more information on Matcha, download the free eBook at www.TheWhiskGuide.com

Please consult a healthcare practitioner if you are pregnant or taking prescription medicine before using this product.

Recommended daily dose

1-5g daily

Storage information: Store in a cool dry place away from sunlight, moisture, and heat. Keep contents dry.

Logos for back of pack:
EU Organic logo with 'GB-ORG-17 Non-EU Agriculture' written directly underneath it.
Vegan logo
Natural Produce Alliance logo
Bazaarly Barcode

Additional deisgn notes:

We have included a design that we like.

The top 2cm will be torn off by the user, so should not contain any key information.

Target Market(s)

High End health and wellness Consumers

Colors
acd036
0455a3
edf8f6

Requirements
Must have
• Stand out on Bazaarly. Show the product to be premium.

```html
<!DOCTYPE html>
<html lang="en">
<head>
<meta charset="utf-8">
<title>Leafwrights Matcha Packs</title>
<link rel="stylesheet" href="https://fonts.googleapis.com/css2?family=Montserrat:wght@700&family=Great+Vibes&family=Playball&family=Quicksand:wght@500&family=Oswald:wght@400&family=Roboto+Condensed:ital@1&family=Noto+Serif:wght@400&family=Yuji+Syuku&display=swap">
<style>
  :root {
    --canvas: #f1f2f1;
    --pack: #ffffff;
    --seal: #ececec;
    --ink: #111111;
    --brand-green: #8cc63f;
    --organic-green: #9ac42a;
    --purple-deep: #33146e;
    --purple-mid: #6a3aa6;
    --purple-light: #efc6f0;
    --blue-deep: #0f2a5c;
    --blue-bright: #1aa3e0;
    --matcha: #6ea22a;
  }
  * { margin: 0; padding: 0; box-sizing: border-box; }
  html, body { width: 1200px; height: 762px; overflow: hidden; background: var(--canvas); }
  .canvas { position: relative; width: 1200px; height: 762px; }
  .pack {
    position: absolute; background: var(--pack); overflow: hidden;
    box-shadow: 0 6px 24px rgba(0,0,0,0.12);
  }
  .pack > * { position: absolute; }
  .seal { left: 0; top: 0; width: 100%; background: var(--seal); }
  .band { top: 0; }
  .grade-bar { left: 0; display: flex; align-items: center; color: #fff; white-space: nowrap; }
  .brand { color: var(--brand-green); font-family: "Quicksand", sans-serif; font-weight: 500; white-space: nowrap; }
  .kanji { color: #fff; font-family: "Yuji Syuku", serif; transform: translateX(-50%); white-space: nowrap; }
  .bowl { border-radius: 50%; }
  .weight { font-family: "Noto Serif", serif; color: var(--ink); transform: translateX(-50%); }

  /* Premium pack */
  .pack--premium { left: 174px; top: 64px; width: 386px; height: 632px; }
  .pack--premium .seal { height: 20px; }
  .pack--premium .band {
    left: 134px; width: 116px; height: 338px;
    background: linear-gradient(180deg, var(--purple-deep) 0%, var(--purple-mid) 25%, var(--purple-light) 44%, var(--purple-mid) 50%, var(--purple-deep) 70%, #2a0f5e 100%);
  }
  .pack--premium .grade-bar {
    top: 150px; width: 250px; height: 34px; padding-left: 38px;
    background: linear-gradient(90deg, #000 0%, #1c2a10 45%, #b8d08c 100%);
    font-family: "Montserrat", sans-serif; font-weight: 700; font-size: 18px; letter-spacing: 2px;
  }
  .pack--premium .brand { left: 262px; top: 122px; font-size: 20px; }
  .pack--premium .title {
    left: 0; width: 386px; top: 200px; text-align: center;
    font-family: "Great Vibes", cursive; font-size: 84px; line-height: 1; color: var(--ink);
  }
  .pack--premium .kanji { left: 192px; top: 284px; font-size: 36px; }
  .pack--premium .tagline {
    left: 0; width: 386px; top: 372px; text-align: center;
    font-family: "Playball", cursive; font-size: 18px; line-height: 1.05; color: var(--ink);
  }
  .pack--premium .bowl { left: 90px; top: 440px; width: 208px; height: 104px; }
  .pack--premium .weight { left: 192px; top: 568px; font-size: 20px; }

  /* Ceremonial pack */
  .pack--ceremonial { left: 696px; top: 250px; width: 270px; height: 442px; }
  .pack--ceremonial .seal { height: 14px; }
  .pack--ceremonial .band {
    left: 98px; width: 72px; height: 236px;
    background: linear-gradient(180deg, var(--blue-deep) 0%, #12407e 30%, var(--blue-bright) 52%, #0f4e92 75%, var(--blue-deep) 100%);
  }
  .pack--ceremonial .grade-bar {
    top: 105px; width: 172px; height: 24px; padding-left: 30px;
    background: linear-gradient(90deg, #000 0%, #222 60%, #8a8a8a 100%);
    font-family: "Oswald", sans-serif; font-size: 13px; letter-spacing: 2px;
  }
  .pack--ceremonial .brand { left: 178px; top: 80px; font-size: 14px; }
  .pack--ceremonial .organic-badge { left: 196px; top: 101px; width: 46px; height: 31px; background: var(--organic-green); }
  .pack--ceremonial .title {
    left: 38px; top: 142px; width: 192px; height: 46px;
    display: flex; justify-content: space-between; align-items: baseline;
    font-family: "Noto Serif", serif; font-size: 46px; line-height: 1; color: var(--ink);
  }
  .pack--ceremonial .kanji { left: 134px; top: 196px; font-size: 26px; }
  .pack--ceremonial .tagline {
    left: 0; width: 270px; top: 256px; text-align: center;
    font-family: "Roboto Condensed", sans-serif; font-style: italic; font-size: 11.5px; line-height: 1.1; color: var(--ink);
  }
  .pack--ceremonial .bowl { left: 60px; top: 302px; width: 152px; height: 76px; }
  .pack--ceremonial .weight { left: 136px; top: 398px; font-size: 15px; }

  .bowl--matcha {
    background: radial-gradient(ellipse at 50% 40%, var(--matcha) 0%, #8dbb3c 35%, #e8ece6 62%, #f7f7f5 100%);
  }
</style>
</head>
<body>
<main class="canvas">

  <section class="pack pack--premium">
    <div class="seal"></div>
    <div class="band"></div>
    <div class="grade-bar">Premium Grade</div>
    <div class="brand">Leafwrights</div>
    <div class="title">Matcha</div>
    <div class="kanji">抹茶</div>
    <p class="tagline">Organic Handpicked, Stoneground<br>Japanese Matcha Green Tea Powder</p>
    <div class="bowl bowl--matcha" role="img" aria-label="Photo of matcha powder heaped in a white ceramic dish"></div>
    <div class="weight">100g</div>
  </section>

  <section class="pack pack--ceremonial">
    <div class="seal"></div>
    <div class="band"></div>
    <div class="grade-bar">Ceremonial Grade</div>
    <div class="brand">Leafwrights</div>
    <div class="organic-badge" aria-label="Organic certification badge"></div>
    <div class="title" aria-label="Matcha"><span>M</span><span>a</span><span>t</span><span>c</span><span>h</span><span>a</span></div>
    <div class="kanji">抹茶</div>
    <p class="tagline">Organic Handpicked, Stoneground<br>Japanese Matcha Green Tea Powder</p>
    <div class="bowl bowl--matcha" role="img" aria-label="Photo of matcha powder heaped in a white ceramic dish"></div>
    <div class="weight">40g</div>
  </section>

</main>
</body>
</html>
```